The Larkspur Initiative WEBSITE DESIGN

Larkspur is a not for profit working in international aid and development. The website needs to be lively not depressing,earthy rather than bling, have a dramatic impact over lightweight. It may be that a black and white with spot colour may be more impacting given the simplicity I want for the site. Larkspur works in partnership with registered NGOs in Asia and Africa. At any one time it will have about five feature projects. The purpose is for people to be able to find out about the projects, the countries, the partner organisations, people's stories and then give people the opportunity to give their financial and volunteer support.

Target Market(s)

First World Donors
All ages but particularly 25 - 55

Industry/Entity Type

Human Rights

Number of Pages Required

5+ page

Font styles to use
Sans Serif

Requirements
Must have
• Simplicity
• Easy access to giving options
• Highlight stories both video and image + copy (sample in attachments)
• Lots of images over copy
Nice to have
• Interest
• Not boring
• May work in black and white with a spot colour or sepia look
Should not have
• Shiny new look
• Dont know how many pages or if it be coded or uncoded - makes no sense to me

```html
<!DOCTYPE html>
<html lang="en">
<head>
<meta charset="utf-8">
<title>The Larkspur Initiative</title>
<link href="https://fonts.googleapis.com/css2?family=Open+Sans:wght@400;600;700&display=swap" rel="stylesheet">
<style>
:root{
  --orange:#f39200;
  --green:#b6c64a;
  --green-dark:#8fa035;
  --ink:#2e2e2e;
  --grey:#6b6b6b;
  --light:#f3f3f1;
  --white:#ffffff;
  --footer:#2b2b2b;
}
*{margin:0;padding:0;box-sizing:border-box}
html,body{width:752px;height:1200px;overflow:hidden}
body{font-family:"Open Sans",Arial,sans-serif;color:var(--ink);background:var(--white);position:relative}
.hero{position:absolute;top:0;left:0;width:752px;height:338px;background:linear-gradient(180deg,#bcc7cf 0%,#9aa0a0 45%,#6b5a4c 100%)}
.topbar{position:absolute;top:0;left:0;width:752px;height:60px;background:rgba(255,255,255,.88)}
.call{position:absolute;top:8px;right:30px;font-size:11px;color:var(--orange);font-weight:600}
.nav{position:absolute;top:28px;right:30px;display:flex;gap:4px}
.nav a{font-size:10px;color:var(--ink);text-decoration:none;padding:5px 8px;text-transform:uppercase}
.nav a.active{border:1px solid #bbb;background:var(--white)}
.brand{position:absolute;top:0;left:75px;width:138px;height:150px;background:var(--white);box-shadow:0 2px 6px rgba(0,0,0,.2);display:flex;flex-direction:column;align-items:center;justify-content:center;gap:10px}
.brand-dot{width:56px;height:56px;border-radius:50%;background:var(--green)}
.brand-name{font-size:15px;font-weight:700;color:var(--orange);text-align:center;line-height:1.15;text-transform:uppercase}
.caption{position:absolute;top:292px;left:200px;width:352px;height:32px;background:rgba(40,40,40,.75);color:var(--white);font-size:15px;display:flex;align-items:center;justify-content:center}
.welcome{position:absolute;top:338px;left:0;width:752px;height:174px;padding:22px 62px 0}
.welcome h1{font-size:22px;font-weight:400}
.welcome h1 span{color:var(--orange);font-weight:700}
.welcome h1 small{color:var(--orange);font-size:8px;letter-spacing:3px;font-weight:600}
.welcome .lead{font-size:11px;font-weight:700;margin-top:12px;width:400px}
.welcome .body{font-size:9px;color:var(--grey);line-height:1.5;width:400px;margin-top:4px}
.btn{display:inline-block;margin-top:10px;background:var(--ink);color:var(--white);font-size:9px;padding:4px 12px;position:relative}
.btn::after{content:"";position:absolute;right:-14px;top:0;width:14px;height:100%;background:var(--orange)}
.aims{position:absolute;top:22px;left:488px;width:220px}
.aim{display:flex;gap:12px;margin-bottom:14px}
.aim-icon{width:38px;height:38px;border-radius:50%;flex:none}
.aim-icon.teal{background:#2d8fb0}
.aim-icon.dark{background:var(--ink)}
.aim h2{font-size:12px;font-weight:700;text-transform:uppercase}
.aim p{font-size:8px;color:var(--grey);line-height:1.45}
.projects{position:absolute;top:512px;left:0;width:752px;height:250px;background:linear-gradient(180deg,#c9d27a,#a9b74a);text-align:center}
.projects h2,.news h2{font-size:20px;font-weight:400;padding-top:16px}
.projects .sub{font-size:10px;color:#3b3b2a;margin-top:4px}
.cards{display:flex;gap:22px;justify-content:center;margin-top:16px}
.card{width:190px}
.card-photo{height:118px}
.card-label{height:26px;background:var(--white);display:flex;justify-content:space-between;align-items:center;font-size:12px;padding-left:10px}
.card-label b{width:26px;height:26px;background:var(--orange);color:var(--white);font-size:18px;line-height:26px;text-align:center;font-weight:400}
.news{position:absolute;top:762px;left:0;width:752px;height:188px;background:var(--light);text-align:center}
.articles{display:flex;gap:30px;justify-content:center;margin-top:14px;text-align:left}
.article{width:320px;display:flex;gap:10px}
.article-photo{width:88px;height:96px;flex:none}
.article h3{font-size:8px;font-weight:700;text-transform:uppercase}
.article p{font-size:8px;color:var(--grey);line-height:1.45;margin-top:3px}
.article .btn{margin-top:6px;font-size:7px;padding:2px 8px}
.give{position:absolute;top:950px;left:0;width:752px;height:188px;display:flex}
.give-panel{flex:1;display:flex;flex-direction:column;align-items:center;justify-content:center;color:var(--white);text-align:center}
.give-panel.left{background:linear-gradient(135deg,#555 0%,#2c2c2c 100%)}
.give-panel.right{background:linear-gradient(135deg,#3c3c3c 0%,#6c6c6c 100%)}
.give-panel h2{font-size:22px;font-weight:600}
.give-panel p{font-size:10px;margin-top:6px;width:180px}
.footer{position:absolute;top:1138px;left:0;width:752px;height:44px;background:var(--green);display:flex;align-items:center;padding:0 40px}
.footer nav{display:flex;gap:22px}
.footer nav a{font-size:9px;color:var(--ink);text-decoration:none;text-transform:uppercase}
.social{margin-left:auto;display:flex;gap:8px;margin-right:40px}
.social span{width:22px;height:22px;border-radius:50%;background:var(--ink)}
.foot-mark{width:30px;height:30px;border-radius:50%;background:var(--green-dark)}
.copy{position:absolute;top:1182px;left:0;width:752px;height:18px;background:var(--footer);color:#bbb;font-size:7px;text-align:center;line-height:18px}
</style>
</head>
<body>
<section class="hero" role="img" aria-label="Photo of a volunteer smiling with a group of children in front of a tent camp"></section>
<header class="topbar">
  <div class="call">Call Us: 555 012 3487</div>
  <nav class="nav">
    <a class="active">Home</a><a>About</a><a>Projects</a><a>Services</a><a>Global Location</a><a>Resources</a><a>Contact Us</a>
  </nav>
</header>
<div class="brand"><span class="brand-dot"></span><span class="brand-name">Larkspur<br>Initiative</span></div>
<div class="caption">Lorem Ipsum Dolor Sit Amet</div>

<section class="welcome">
  <h1>Welcome To <span>LARKSPUR</span> <small>INITIATIVE</small></h1>
  <p class="lead">Lorem ipsum dolor sit amet, ex vim quem primis, Quot suavitate</p>
  <p class="body">Lorem ipsum dolor sit amet, ex vim quem primis. Quot suavitate molestiae eu usu. Reformidans sit ut, dolor adhuc nusquam mel te, nam elit viris principes. Te vel erant semper, in pro tempor putent, vitae soluta ancillae ex vis. Ea per tota amet fabulas, nam ut odio dicunt.</p>
  <span class="btn">Read More</span>
  <div class="aims">
    <div class="aim"><span class="aim-icon teal"></span><div><h2>Our Vision</h2><p>Lorem ipsum dolor sit amet, ex vim quem primis. Quot suavitate molestiae eu usu. Referre adhuc ut.</p></div></div>
    <div class="aim"><span class="aim-icon dark"></span><div><h2>Our Mission</h2><p>Lorem ipsum dolor sit amet, ex vim quem primis. Quot suavitate molestiae eu usu. Referre adhuc ut.</p></div></div>
  </div>
</section>

<section class="projects">
  <h2>Current Projects</h2>
  <p class="sub">Lorem ipsum dolor sit amet, ex vim quem primis, Quot suavitate</p>
  <div class="cards">
    <div class="card"><div class="card-photo" role="img" aria-label="Photo of colourful woven fabrics" style="background:linear-gradient(135deg,#c9504a,#3f7fb0,#e2b13a)"></div><div class="card-label">Lotus Cambodia<b>+</b></div></div>
    <div class="card"><div class="card-photo" role="img" aria-label="Photo of a community group gathered outdoors" style="background:linear-gradient(135deg,#8a6a4a,#c08a5a,#6a7a4a)"></div><div class="card-label">Hillside Rwanda<b>+</b></div></div>
    <div class="card"><div class="card-photo" role="img" aria-label="Photo of people under a canopy in a village" style="background:linear-gradient(135deg,#6a88a8,#b04a40,#a08a6a)"></div><div class="card-label">Sunrise Kenya<b>+</b></div></div>
  </div>
</section>

<section class="news">
  <h2>News / Stories from Projects</h2>
  <div class="articles">
    <div class="article"><div class="article-photo" role="img" aria-label="Photo of a woman at work in a project village" style="background:linear-gradient(135deg,#7a6a5a,#b59a7a)"></div><div><h3>Ongoing stories and voices from overseas</h3><p>Lorem ipsum dolor sit amet, ex vim quem primis. Quot suavitate molestiae eu usu. Referre eleifend ei sea, dolor adhuc nusquam mel te, nam elit viris principes et.</p><span class="btn">Read More</span></div></div>
    <div class="article"><div class="article-photo" role="img" aria-label="Photo of children seated in a classroom" style="background:linear-gradient(135deg,#9a7a5a,#5a4a3a)"></div><div><h3>Articles about aid and development</h3><p>Lorem ipsum dolor sit amet, ex vim quem primis. Quot suavitate molestiae eu usu. Referre eleifend ei sea, dolor adhuc nusquam mel te, nam elit viris principes et.</p><span class="btn">Read More</span></div></div>
  </div>
</section>

<section class="give">
  <div class="give-panel left" role="img" aria-label="Black and white photo of donors and children"><h2>Online Giving</h2><p>Lorem ipsum dolor sit amet, ex vim quem primis, Quot suavitate</p></div>
  <div class="give-panel right" role="img" aria-label="Black and white photo of volunteers with a child"><h2>Volunteer Vacancies</h2><p>Lorem ipsum dolor sit amet, ex vim quem primis, Quot suavitate</p></div>
</section>

<footer class="footer">
  <nav><a>Home</a><a>About</a><a>Projects</a><a>Services</a><a>Global Location</a><a>Resources</a><a>Contact Us</a></nav>
  <div class="social"><span></span><span></span><span></span></div>
  <span class="foot-mark"></span>
</footer>
<div class="copy">Copyright © 2013 · The Larkspur Initiative · All Rights Reserved.</div>
</body>
</html>
```